Lawyer health website (wordpress design) to improve well being/health for lawyers

I need a webdesign for personal website called www.plumcounselhub.net. Website will be focused on health/wellness for my profession (lawyers) and other professionals too. Will have a blog on a separate page, a calorie counter on first page, and forums for me to begin topics and users to post. Also want the ability to add and delete information on a consistent basis...especially news articles related to my profession. I will want the homepage to include both health related information - different articles and articles related to the professionl. Need a tab to link my vitaloop site. I like format of www.dailyvigornest.com and www.munchtallyhub.com and www.sourbarrister.com. My website will have a mix of these themes and will not be too sarcastic (sourbarrister) but fun and healthy, a place for other attorneys and professionals to go to support eachother in health and wellness and their profession. Will need these things for the website:

(1) Responsive design (can be viewed on mobile phones, ipads, ect.)
(2)Cross browser support
(3) Custom background and colors
(4) Allow admin to post on front end and to add pages and delete and add info
(5) All post will have social media share
(6)Admin can control what is posted on page so if someone comments admin can review it before its posted on articles...forums no control over that. If admin wants to I can change the review function.
(7) Users can sign in with social media accounts or create a user name and password
(8) I am a female attorney so I prefer it be a bit more feminine but I will encourage males to follow the page as well.
(9) Feature attorney of the month or week on a page. I think this would be cool to do on a separate page highlighting an attorney, their practice area, their fitness goals ect.

Target Market(s)

Attorneys

Industry/Entity Type

Health

Coding

Coded - Design and coding required

Number of Pages Required

5+ page

Font styles to use
Serif

Colors
cadf82
85cae6
0355a3
00a990

Requirements
Must have
• Home page with "Featured attorney" section in a corner of page so users can click on that pic to learn about that "Feautured attorney" and how he/she stays fit. Also, calorie counter on home page, blog, Contact Us Page, and Forum Page.
• I MUST HAVE ABILITY TO ADD/DELETE CONTENT ON MY WEBSITE ON A CONSISTENT BASIS.

```html
<!DOCTYPE html>
<html lang="en">
<head>
<meta charset="utf-8">
<title>Plum Counsel Hub</title>
<link href="https://fonts.googleapis.com/css2?family=Bree+Serif&family=Lato:ital,wght@0,400;0,700;1,400&family=PT+Serif&display=swap" rel="stylesheet">
<style>
:root{
  --lime:#cadf82;
  --sky:#85cae6;
  --navy:#0355a3;
  --teal:#00a990;
  --ink:#222;
  --text:#333;
  --muted:#8aa;
  --footer:#262626;
  --footer-low:#2e2e2e;
  --footer-text:#bdbdbd;
}
*{box-sizing:border-box;margin:0;padding:0}
html,body{width:801px;height:1200px;overflow:hidden;background:#fff}
body{position:relative;font-family:'Lato',sans-serif;color:var(--text)}
.abs{position:absolute}

/* hero */
.hero-photo{left:0;top:0;width:801px;height:375px;background:linear-gradient(100deg,#dfe6ea 0%,#c9d3d8 30%,#e8c6bb 45%,#cfd9de 60%,#aebcc4 85%,#8d9ea8 100%)}
.topstrip{left:0;top:0;width:801px;height:31px;background:rgba(255,255,255,.55)}
.search{left:482px;top:5px;width:156px;height:20px;border:1px solid #c8c8c8;background:rgba(255,255,255,.8);font:italic 8px 'PT Serif',serif;color:#aaa;padding:5px 6px}
.search svg{position:absolute;right:4px;top:3px}
.login{left:652px;top:5px;width:61px;height:21px;background:var(--sky);color:#fff;font:12px 'PT Serif',serif;text-align:center;line-height:21px;border-radius:2px}
.navbar{left:0;top:31px;width:801px;height:31px;background:var(--lime)}
.nav{left:280px;top:31px;height:31px;display:flex;align-items:center;font:11.5px 'PT Serif',serif;color:var(--ink)}
.nav span{padding:0 14px;border-left:1px solid #a6bd5a}
.nav span:first-child{border-left:0}
.logo{left:88px;top:16px;width:182px;height:62px;background:#fff;box-shadow:0 1px 4px rgba(0,0,0,.2);display:flex;align-items:center;justify-content:center;gap:6px;font:18px 'Bree Serif',serif;color:var(--teal)}
.logo i{width:10px;height:10px;background:var(--lime);display:block}
.caption{left:87px;top:305px;width:383px;height:37px;background:linear-gradient(90deg,rgba(133,202,230,.8),rgba(133,202,230,0));font:italic 22px 'Bree Serif',serif;color:#fff;padding:4px 8px;text-shadow:0 1px 2px rgba(0,0,0,.3)}

/* calorie counter */
.calc{left:515px;top:116px;width:198px;height:211px;background:rgba(133,202,230,.75)}
.calc-head{height:30px;background:var(--teal);color:#fff;font:13px 'Bree Serif',serif;text-align:center;line-height:30px}
.calc label{position:absolute;font:bold 8px 'Lato',sans-serif;color:#fff;text-transform:uppercase}
.field{position:absolute;height:22px;background:#fff;border:1px solid #ddd;font:italic 9px 'Lato',sans-serif;color:#aaa;padding:5px 6px}
.field b{position:absolute;right:0;top:0;width:12px;height:20px;border-left:1px solid #ddd}
.go{position:absolute;left:22px;top:172px;width:155px;height:28px;background:var(--teal);color:#fff;font:bold 11px 'Lato',sans-serif;text-align:center;line-height:28px;border-radius:2px;box-shadow:0 2px 0 #00806d}

/* call band */
.callband{left:0;top:375px;width:801px;height:49px;background:linear-gradient(#f1f1f1,#dcdcdc);border-bottom:1px solid #ccc}
.call{left:90px;top:387px;font:italic 16px 'Bree Serif',serif;color:var(--navy)}
.call em{font-size:21px;color:var(--teal)}
.vitaloop{left:496px;top:387px;width:217px;height:28px;background:var(--lime);color:var(--teal);font:13px 'Lato',sans-serif;text-align:center;line-height:28px;box-shadow:0 2px 3px rgba(0,0,0,.25)}
.vitaloop strong{color:var(--navy);font-weight:400}

/* sections */
h2{position:absolute;font:400 14.5px 'Lato',sans-serif;color:var(--ink);text-transform:uppercase}
h2 span{color:var(--navy)}
.rule{position:absolute;height:1px;background:#ddd}
.rule::before{content:"";position:absolute;left:0;top:-1px;width:64px;height:2px;background:var(--navy)}
.welcome-text{left:88px;top:498px;width:306px;font-size:8.4px;line-height:14px;color:#333}
.readmore{left:88px;top:592px;width:74px;height:20px;background:var(--teal);color:#fff;font:8.5px 'Bree Serif',serif;text-align:center;line-height:20px;border-radius:2px}
.featured{left:418px;top:455px;width:295px;height:168px;background:var(--sky);border:1px solid #5fb2d6}
.featured h3{position:absolute;left:11px;top:8px;font:400 14px 'Lato',sans-serif;color:#fff}
.featured .line{position:absolute;left:11px;top:30px;width:270px;height:1px;background:rgba(255,255,255,.6)}
.attorney-photo{position:absolute;left:13px;top:45px;width:157px;height:109px;border:2px solid #fff;background:linear-gradient(90deg,#d7dee3,#6d4a3c 45%,#2b2b2b 60%,#e5ebee)}
.featured p{position:absolute;left:179px;top:45px;width:106px;font-size:8.2px;line-height:12.2px;color:#fff;letter-spacing:.3px}

.arrows{position:absolute;display:flex;gap:7px}
.arrows i{width:17px;height:16px;border:1px solid #bbb;font:normal 8px 'Lato',sans-serif;color:#555;text-align:center;line-height:14px;display:block}

.news{position:absolute;left:88px;width:310px}
.thumb{position:absolute;left:0;top:0;width:62px;height:51px}
.news .date{position:absolute;left:77px;top:1px;font:italic 9px 'Lato',sans-serif;color:var(--sky)}
.news p{position:absolute;left:77px;top:12px;width:232px;font-size:8px;line-height:11.5px;color:#333}
.news a,.blog a{color:var(--teal);text-decoration:underline}

.blog{position:absolute;left:419px;width:294px;height:104px}
.blog .photo{position:absolute;left:0;top:0;width:105px;height:104px}
.badge{position:absolute;left:109px;top:0;width:24px;height:21px;background:var(--teal);color:#fff;font:bold 8px/8px 'Lato',sans-serif;padding:2px 3px}
.badge sup{font-size:5px}
.blog h4{position:absolute;left:140px;top:2px;font:400 11px 'Lato',sans-serif;color:var(--sky)}
.blog p{position:absolute;left:110px;top:29px;width:184px;font-size:8.3px;line-height:12.2px;color:#333}
.share{position:absolute;left:113px;top:88px;display:flex;gap:4px}
.share i{width:16px;height:16px;display:block;border-radius:1px}
.comments{position:absolute;left:208px;top:88px;width:66px;height:16px;border:1px solid #ccc;background:#f6f6f6;font:bold 6.5px 'Lato',sans-serif;color:#333;line-height:14px;padding-left:19px}
.comments svg{position:absolute;left:5px;top:3px}
.out{position:absolute;left:279px;top:88px;width:15px;height:16px;background:#f15a24}
.out svg{position:absolute;left:4px;top:4px}

/* footer */
.footer{left:0;top:988px;width:801px;height:121px;background:var(--footer);color:var(--footer-text)}
.footer h5{position:absolute;font:400 12px 'Lato',sans-serif;color:#fff;text-transform:uppercase}
.footer p{position:absolute;font-size:8.4px;line-height:16px}
.vsep{position:absolute;top:18px;width:1px;height:87px;background:#444}
.newsletter{position:absolute;left:306px;top:53px;width:189px;height:29px;border:1px solid #555;font-size:8.5px;color:#aaa;padding:9px 10px}
.newsletter svg{position:absolute;right:12px;top:11px}
.footer-low{left:0;top:1109px;width:801px;height:91px;background:var(--footer-low);border-top:1px solid #444}
.footnav{position:absolute;left:0;top:16px;width:801px;text-align:center;font-size:9px;color:#bbb}
.footnav span{padding:0 8px}
.socials{position:absolute;left:358px;top:46px;display:flex;gap:7px}
.socials i{width:15px;height:15px;border-radius:50%;background:#666;display:block}
.socials i:first-child{background:var(--sky)}
.copy{position:absolute;left:0;top:71px;width:801px;text-align:center;font-size:8.5px;color:#aaa}
</style>
</head>
<body>

<div class="abs hero-photo" role="img" aria-label="Smiling woman exercising with dumbbells in a bright gym"></div>
<div class="abs topstrip"></div>
<div class="abs search">SEARCH
  <svg width="12" height="12" viewBox="0 0 12 12"><circle cx="5" cy="5" r="3.8" fill="none" stroke="#555" stroke-width="1.3"/><line x1="8" y1="8" x2="11" y2="11" stroke="#555" stroke-width="1.4"/></svg>
</div>
<div class="abs login">LOGIN</div>
<div class="abs navbar"></div>
<nav class="abs nav"><span>HOME</span><span>FEATURED ATTORNEY</span><span>BLOG</span><span>FORUM</span><span>CONTACT</span></nav>
<div class="abs logo"><i></i>Plum Counsel Hub</div>
<div class="abs caption">Best way to lose your weight</div>

<form class="abs calc">
  <div class="calc-head">CALORIE COUNTER</div>
  <label style="left:21px;top:40px">Hight</label>
  <div class="field" style="left:21px;top:54px;width:74px">ft<b></b></div>
  <div class="field" style="left:103px;top:54px;width:74px">in<b></b></div>
  <label style="left:21px;top:83px">Weight</label>
  <label style="left:105px;top:83px">Age</label>
  <div class="field" style="left:21px;top:97px;width:74px">lbs<b></b></div>
  <div class="field" style="left:103px;top:97px;width:74px"><b></b></div>
  <label style="left:21px;top:126px">Gender</label>
  <div class="field" style="left:21px;top:140px;width:158px;color:#333">Female<b></b></div>
  <div class="go">GO</div>
</form>

<div class="abs callband"></div>
<div class="abs call">For any query call us on - <em>123-555-0148</em></div>
<div class="abs vitaloop">Click here to vist our <strong>Vitaloop</strong> site</div>

<h2 style="left:88px;top:463px"><span>Welcome to</span> Plum Counsel Hub</h2>
<div class="rule" style="left:88px;top:485px;width:306px"></div>
<p class="abs welcome-text">Lorem ipsum dolor sit amet, consectetur adipiscing elit. Aenean sodales diam quis velit pellentesque vehicula. Donec luctus justo aliquet est volutpat, sed tincidunt odio pretium. Sed id est ultrici rutrum arcu pretium, porttitor enim. Integer quis luctus ligula. Donec id scelerisque lorem. Duis vehicu nulla at tristique semper. Vivamus id volutpat ipsum, eget fermentum nunc.</p>
<div class="abs readmore">READ MORE</div>

<section class="abs featured">
  <h3>FEATURED ATTORNEY</h3>
  <div class="line"></div>
  <div class="attorney-photo" role="img" aria-label="Portrait of the featured attorney in an office"></div>
  <p>Fusce elementum, nulla vel pellentes conse quat, ante nulla hendrerit arcu, ac tincidunt mauris lacus sed leo. vamus suscipit molestie vestibulum. Lorem ipsum dolor site amet,</p>
</section>

<h2 style="left:87px;top:683px"><span>Latest</span> News</h2>
<div class="arrows" style="left:354px;top:683px"><i>&laquo;</i><i>&raquo;</i></div>
<div class="rule" style="left:87px;top:708px;width:309px"></div>

<div class="news" style="top:731px">
  <div class="thumb" role="img" aria-label="Bowl of fresh vegetables" style="background:linear-gradient(135deg,#7aa83c,#e8783a,#c9383a)"></div>
  <span class="date">25.03.2015</span>
  <p><b>Lorem ipsum dolor</b> sit amet, consec teteur adipi scing. Praesent vestibu. lum molestie lacuiirhs. Aenean non ummy hendreriauris. Phasellllus. <a>More</a></p>
</div>
<div class="news" style="top:800px">
  <div class="thumb" role="img" aria-label="Woman lifting small dumbbells" style="background:linear-gradient(135deg,#f2f2f2,#d8c4b4,#3d8ccc)"></div>
  <span class="date">25.03.2015</span>
  <p><b>Lorem ipsum dolor</b> sit amet, consec teteur adipi scing. Praesent vestibu. lum molestie lacuiirhs. Aenean non ummy hendreriauris. Phasellllus. <a>More</a></p>
</div>
<div class="news" style="top:869px">
  <div class="thumb" role="img" aria-label="Woman stretching on a yoga mat" style="background:linear-gradient(135deg,#f3e6e2,#e99ab0,#6cb4d8)"></div>
  <span class="date">25.03.2015</span>
  <p><b>Lorem ipsum dolor</b> sit amet, consec teteur adipi scing. Praesent vestibu. lum molestie lacuiirhs. Aenean non ummy hendreriauris. Phasellllus. <a>More</a></p>
</div>

<h2 style="left:420px;top:683px"><span>Latest</span> Blog</h2>
<div class="arrows" style="left:671px;top:683px"><i>&laquo;</i><i>&raquo;</i></div>
<div class="rule" style="left:420px;top:708px;width:293px"></div>

<article class="blog" style="top:720px">
  <div class="photo" role="img" aria-label="Older woman in a fitness class with hand weights" style="background:linear-gradient(135deg,#c9c2b8,#e8d6c4,#9cc3a8)"></div>
  <div class="badge">17<sup>th</sup><br>Apr</div>
  <h4>Lorem ipsum dolor sit amet,</h4>
  <p>Fusce elementum, nulla vel pellentes conse quat, ante nulla hendrerit arcu, ac tincidunt mauris lacus sed leo. vamus suscipit molestie vestibulum. Lorem ipsum dolor sit amet,</p>
  <div class="share"><i style="background:var(--navy)"></i><i style="background:var(--sky)"></i><i style="background:var(--teal)"></i></div>
  <div class="comments"><svg width="9" height="8" viewBox="0 0 9 8"><path d="M1 1h7v4H4L2 7V5H1z" fill="none" stroke="#333" stroke-width=".9"/></svg>Comments (66)</div>
  <div class="out"><svg width="8" height="8" viewBox="0 0 8 8"><path d="M3 1H1v6h6V5M4 4l3-3M5 1h2v2" fill="none" stroke="#fff" stroke-width="1"/></svg></div>
</article>

<article class="blog" style="top:851px">
  <div class="photo" role="img" aria-label="Plate of fruit and vegetables held in hands" style="background:radial-gradient(circle at 50% 45%,#f4d04a 0,#8c3a6a 30%,#e65a3a 45%,#f2f2f2 65%,#d9dde0)"></div>
  <div class="badge">15<sup>th</sup><br>Apr</div>
  <h4>Lorem ipsum dolor sit amet,</h4>
  <p>Fusce elementum, nulla vel pellentes conse quat, ante nulla hendrerit arcu, ac tincidunt mauris lacus sed leo. vamus suscipit molestie vestibulum. Lorem ipsum dolor sit amet,</p>
  <div class="share"><i style="background:var(--navy)"></i><i style="background:var(--sky)"></i><i style="background:var(--teal)"></i></div>
  <div class="comments"><svg width="9" height="8" viewBox="0 0 9 8"><path d="M1 1h7v4H4L2 7V5H1z" fill="none" stroke="#333" stroke-width=".9"/></svg>Comments (66)</div>
  <div class="out"><svg width="8" height="8" viewBox="0 0 8 8"><path d="M3 1H1v6h6V5M4 4l3-3M5 1h2v2" fill="none" stroke="#fff" stroke-width="1"/></svg></div>
</article>

<footer class="abs footer">
  <h5 style="left:89px;top:21px">Plum Counsel Hub</h5>
  <p style="left:88px;top:40px;width:170px">000 Vestibulum suscipit tellus fermentum nibh blandit congue In ipsum pretium suscipit ut quam.<br>000 000</p>
  <div class="vsep" style="left:280px"></div>
  <h5 style="left:328px;top:21px">Sign up for newsletter</h5>
  <div class="newsletter">Enter your email here
    <svg width="8" height="7" viewBox="0 0 8 7"><path d="M0 3.5h7M4.5 1l2.5 2.5L4.5 6" fill="none" stroke="#ccc" stroke-width="1"/></svg>
  </div>
  <div class="vsep" style="left:521px"></div>
  <h5 style="left:657px;top:21px">Reach us</h5>
  <p style="right:88px;top:40px;text-align:right"><b style="color:#fff">m:</b> (123) 555 0190<br>(123) 555 0191<br><b style="color:#fff">o:</b> (123) 555 0192<br><b style="color:#fff">e:</b> info@plumcounselhub.net</p>
</footer>
<div class="abs footer-low">
  <div class="footnav"><span>HOME</span>|<span>FEATURED ATTORNEY</span>|<span>BLOG</span>|<span>FORUM</span>|<span>CONTACT</span></div>
  <div class="socials"><i></i><i></i><i></i><i></i></div>
  <div class="copy">&copy; 2015 PLUM COUNSEL HUB | &nbsp;All Rights reserved.</div>
</div>

</body>
</html>
```